"Career in Gradimar" | Poster design

We need a "We are hiring" poster design. We are a construction company based in Croatia and we are looking for 3 categories of construction workers. We want moder, serious and powerful poster . In attachment you can find our logo. The font of a text that is used in logo design is "nexa bold".

At the bottom (or where designer can see it) will be description of general condition. The poster must be simple and clear.

Target Market(s)

Wide range of employment

Industry/Entity Type

Construction Company

Colors

Designer to choose colors to be used in the design.

Requirements
Must have
• The text in poster that will be needed is "Mason/carpenter job", "Steel-bender job" and "Auxiliary worker". This terms may be wrong, but it will be translated in local language. Under all of them will be a short descrtiption row, and one row of salary. This is for all three categories.
• At the bottom (or where designer can see it) will be description of general condition. The poster must be simple and clear.

```html
<!DOCTYPE html>
<html lang="en">
<head>
<meta charset="utf-8">
<title>Gradimar – We're Hiring</title>
<link rel="stylesheet" href="https://fonts.googleapis.com/css2?family=Source+Sans+3:wght@400;700;800&display=swap">
<style>
  :root {
    --navy: #173247;
    --orange: #f0874a;
    --white: #ffffff;
    --ink: #1d2b36;
    --sky-light: #dbe6ee;
    --sky-mid: #7e9fbb;
    --tower-blue: #2f5f8c;
  }
  * { margin: 0; padding: 0; box-sizing: border-box; }
  html, body { width: 776px; height: 1200px; overflow: hidden; background: var(--navy); }
  .poster {
    position: relative;
    width: 776px;
    height: 1200px;
    background: var(--navy);
    font-family: "Source Sans 3", "Myriad Pro", sans-serif;
    color: var(--white);
    overflow: hidden;
  }
  .skyline {
    position: absolute;
    left: 565px; top: 0;
    width: 211px; height: 1200px;
    background: linear-gradient(160deg, var(--sky-light) 0%, var(--sky-mid) 40%, var(--tower-blue) 75%, #132a40 100%);
  }
  .brand-box {
    position: absolute;
    left: 150px; top: 25px;
    width: 263px; height: 157px;
    background: var(--white);
    display: flex;
    flex-direction: column;
    align-items: center;
    justify-content: center;
    gap: 10px;
  }
  .brand-name {
    display: flex;
    align-items: center;
    gap: 10px;
    font-weight: 700;
    font-size: 34px;
    letter-spacing: 1px;
    color: var(--orange);
    text-transform: uppercase;
  }
  .brand-square { width: 22px; height: 22px; background: var(--orange); }
  .brand-tagline {
    font-size: 10px;
    font-weight: 700;
    color: var(--ink);
    letter-spacing: 0.3px;
  }
  .headline {
    position: absolute;
    left: 73px; top: 248px;
    font-size: 104px;
    font-weight: 800;
    line-height: 108px;
    letter-spacing: 1px;
  }
  .job { position: absolute; left: 73px; width: 470px; }
  .job-title {
    font-size: 40px;
    font-weight: 700;
    color: var(--orange);
    line-height: 48px;
    margin-bottom: 8px;
  }
  .job-desc, .job-salary { font-size: 26px; line-height: 33px; }
  .job-salary small { font-size: 18px; }
  .job-salary.strong { font-weight: 700; }
  .job--mason { top: 490px; }
  .job--steel { top: 696px; }
  .job--aux { top: 951px; }
  .footer-band {
    position: absolute;
    left: 0; top: 1165px;
    width: 565px; height: 35px;
    background: var(--orange);
  }
</style>
</head>
<body>
<main class="poster">
  <div class="skyline" role="img" aria-label="Upward view of glass skyscrapers against a pale sky, toned in blue"></div>

  <div class="brand-box">
    <div class="brand-name"><span class="brand-square"></span>Gradimar</div>
    <div class="brand-tagline">IZVOĐENJE I VOĐENJE GRAĐEVINSKIH RADOVA</div>
  </div>

  <h1 class="headline">WE’RE<br>HIRING!</h1>

  <section class="job job--mason">
    <h2 class="job-title">Mason/Carpenter</h2>
    <p class="job-desc">Repairs, maintains and alters buildings, retaining walls and other brick or stone edifices.</p>
    <p class="job-salary strong">SALARY:&nbsp; 45 kn <small>(HRK)</small>/hr</p>
  </section>

  <section class="job job--steel">
    <h2 class="job-title">Steel Bender</h2>
    <p class="job-desc">supports fabrication operations by processing rolled steel for straightening and bending to project specifications.</p>
    <p class="job-salary">SALARY:&nbsp; 35 kn <small>(HKR)</small>/hr</p>
  </section>

  <section class="job job--aux">
    <h2 class="job-title">Auxiliary Worker</h2>
    <p class="job-desc">Assists tradesmen and machine operators in construction projects.</p>
    <p class="job-salary">SALARY:&nbsp; 24 kn <small>(HKR)</small>/hr</p>
  </section>

  <div class="footer-band"></div>
</main>
</body>
</html>
```